WATTLE HILL PRIMARY SCHOOL - WHPS STATIONARY and Promo Pack

Stationary Design

We are a Western Australian Independent Public Primary School called Wattle Hill Primary School.

We are looking for a new fresh and modern stationary design that reflects our innovative open minded approach.

The school colours are in the teak, turquoise range, basically ocean colours as the school is literally 3 minutes away from the beach and has ocean views.

Feel free to incorporate the school motto: Be Your Best
Feel also free to incorporate our values: Respect, Resilience, Cooperation, Responsibility, Tolerance and Excellence

LIST of DELIVERABLES:

#1: Brand identity elements:
• business card

• stationary - basic package including

o letterhead (print ready)
o envelope design
 DL 110 x 220
 DLX 120 x 235
 A4 229 x 324 and (all print ready)
o template for invoices (delivered as PDF file and Word file)
o cover page for annual report (digital file)
o Notepad A4

• PowerPoint template (delivered as PP file)

• Social media banners & logo avatars (delivered as digital files. Facebook, twitter, pinterest, instagram, google plus)

• With compliment slip (DL size - 210mmx 99mm)

• Thank you card (A6)

• A2 poster background (420mm x 594mm)

#2: Brand promotion elements:

• Staff -T - shirt design - long sleeve and short sleeve polo - (Delivered as mock up and digital file / vector)

• Sport banner (roughly 1800mm x 3000) – needs to be in a darker colour please

• Featherbanner (196 x600mm) compare sketch

Industry/Entity Type

School

Contact Information for Business Card

compare provided sample - all info on that one needs to be used please

Colors
85abd2
0355a3
85acd3
eaf1f7
00a990
33b8a4
87cfc6
cfeae6
cee9f5

Requirements
Must have
• LIST of DELIVERABLES:
• #1: Brand identity elements:
• • business card
• • stationary - basic package including
• o letterhead (print ready)
• o envelope design
•  DL 110 x 220
•  DLX 120 x 235
•  A4 229 x 324 and (all print ready)
• o template for invoices (delivered as PDF file and Word file)
• o cover page for annual report (digital file)
• o Notepad A4
• • PowerPoint template (delivered as PP file)
• • Social media banners & logo avatars (delivered as digital files. Facebook, twitter, pinterest, instagram, google plus)
• • With compliment slip (DL size - 210mmx 99mm)
• • Thank you card (A6)
• • A2 poster background (420mm x 594mm)
• #2: Brand promotion elements:
• • Staff -T - shirt design - long sleeve and short sleeve polo - (Delivered as mock up and digital file / vector)
• • Sport banner (roughly 1800mm x 3000) – needs to be in a darker colour please
• • Featherbanner (196 x600mm) compare sketch

```html
<!DOCTYPE html>
<html lang="en">
<head>
<meta charset="utf-8">
<title>Wattle Hill Primary – Thank You Card</title>
<link rel="stylesheet" href="https://fonts.googleapis.com/css2?family=Della+Respira&family=Open+Sans:wght@300;700&family=Pinyon+Script&display=swap">
<style>
  :root {
    --paper: #ffffff;
    --card-bg: #cfeae6;
    --sea-light: #87cfc6;
    --sea-mid: #33b8a4;
    --sea-deep: #00a990;
    --sky-blue: #85abd2;
    --navy-teal: #175b73;
    --ink-green: #0f4a3f;
    --rule: #eaf1f7;
  }
  * { margin: 0; padding: 0; box-sizing: border-box; }
  html, body {
    width: 1200px; height: 742px;
    overflow: hidden;
    background: var(--paper);
  }
  .card {
    position: absolute;
    left: 36px; top: 36px;
    width: 1133px; height: 673px;
    background: var(--card-bg);
    overflow: hidden;
  }
  .wave-art {
    position: absolute;
  }
  .wave-art--left {
    left: -200px; top: -100px;
    width: 700px; height: 900px;
    background:
      radial-gradient(closest-side at 40% 45%, rgba(133,171,210,0.7) 0%, rgba(133,171,210,0.35) 50%, rgba(133,171,210,0) 100%),
      radial-gradient(closest-side at 45% 80%, rgba(135,207,198,0.8) 0%, rgba(135,207,198,0) 100%);
  }
  .wave-art--right {
    left: 640px; top: 140px;
    width: 620px; height: 700px;
    background:
      radial-gradient(closest-side at 55% 65%, rgba(0,169,144,0.85) 0%, rgba(51,184,164,0.6) 40%, rgba(135,207,198,0.4) 70%, rgba(135,207,198,0) 100%);
  }
  .top-rule {
    position: absolute;
    left: 234px; top: 62px;
    width: 680px; height: 1px;
    background: var(--rule);
  }
  .school-watermark {
    position: absolute;
    left: 36px; top: 22px;
    font-family: "Open Sans", sans-serif;
    font-weight: 300;
    font-size: 150px;
    line-height: 135px;
    color: var(--sky-blue);
    opacity: 0.3;
    letter-spacing: 2px;
  }
  .school-watermark span { display: block; }
  .school-watermark .line-2 { padding-left: 250px; }
  .school-name {
    position: absolute;
    left: 381px;
    width: 400px;
    text-align: center;
    font-family: "Open Sans", sans-serif;
    font-weight: 700;
    font-size: 44px;
    line-height: 52px;
    color: var(--navy-teal);
    letter-spacing: 1px;
  }
  .school-name--top { top: 70px; }
  .school-name--bottom { top: 400px; }
  .school-mark {
    position: absolute;
    left: 446px; top: 130px;
    width: 270px; height: 270px;
    border-radius: 50%;
    background: var(--navy-teal);
  }
  .thank-you {
    position: absolute;
    left: 98px; top: 440px;
    font-family: "Della Respira", serif;
    font-weight: 400;
    font-size: 74px;
    line-height: 86px;
    color: var(--ink-green);
  }
  .tagline {
    position: absolute;
    left: 110px; top: 540px;
    font-family: "Pinyon Script", cursive;
    font-size: 40px;
    line-height: 46px;
    color: var(--ink-green);
    white-space: nowrap;
  }
</style>
</head>
<body>
  <main class="card">
    <div class="wave-art wave-art--left" role="img" aria-label="Stylised curling ocean waves in soft blue and seafoam tones"></div>
    <div class="wave-art wave-art--right" role="img" aria-label="Stylised curling ocean waves in turquoise and teal tones"></div>
    <div class="top-rule"></div>
    <p class="school-watermark" aria-hidden="true">
      <span class="line-1">WATTLE</span>
      <span class="line-2">HILL</span>
      <span class="line-3">PRIMARY</span>
    </p>
    <p class="school-name school-name--top">WATTLE HILL</p>
    <div class="school-mark" aria-hidden="true"></div>
    <p class="school-name school-name--bottom">PRIMARY</p>
    <h1 class="thank-you">Thank You</h1>
    <p class="tagline">Your Excellence allow us to be our best</p>
  </main>
</body>
</html>
```